Playing Card Design for Magician's Business Card

Hello! I am looking for a two-sided design for a business card.
The back of the card look like the back of a playing card and includes the following text:
Dorian Feldhaus
www.FeldWonders.com
BACK:
Please - focus most of your time and effort on the BACK DESIGN.
Make it look like a playing card.
I plan to use this design to print up custom playing cards that I use in my show and give away to guests.
No Bunnies No Top Hats!
Not for kids. This is for sophisticated sleight of hand performed for adults.
Mood: Slick, elegant + fun.
See the attached samples of cards I like.
FRONT:
Not much text required ... Please leave plenty of blank space - minimalist.
The front of the card will have
First Name
Website
Phone Number
Email Address
Target Market(s)
Event Planners
Targeting corporate special events and private parties.
Industry/Entity Type
Magician
Contact Information for Business Card
Dorian Feldhaus
Illusionist
www.FeldWonders.com
Colors
Designer to choose colors to be used in the design.
Requirements
Must have
- Back must look like a playing card back.
- BACK MUST INCLUDE the following text:
- Dorian Feldhaus
- www.FeldWonders.com
Nice to have
- Symmetrical Design for back so the card looks the same if upside down.
- Please see "All Seeing Eye" design attached. Remove the Latin phrase and replace with Dorian (top left) Feldhaus (top right)
- FeldWonders.com (Lower middle)
Should not have
- Bunny Rabbits
- Top Hats
- Kids ....

```html
<!DOCTYPE html>
<html lang="en">
<head>
<meta charset="utf-8">
<title>Dorian Feldhaus – Illusionist Card</title>
<link rel="stylesheet" href="https://fonts.googleapis.com/css2?family=Norican&family=Dancing+Script:wght@500&display=swap">
<style>
  :root {
    --stage: #14151a;
    --card: #bacfca;
    --ink: #141518;
    --ink-soft: #3a4341;
    --gold-light: #fff35a;
    --gold: #e8c51a;
    --gold-deep: #a8860c;
    --shadow: #1d2220;
  }
  * { margin: 0; padding: 0; box-sizing: border-box; }
  html, body { width: 848px; height: 1200px; overflow: hidden; background: var(--stage); }
  .canvas { position: relative; width: 848px; height: 1200px; background: var(--stage); }

  .card {
    position: absolute;
    left: 265px;
    width: 342px;
    height: 444px;
    background: var(--card);
    overflow: hidden;
  }
  .card--front { top: 76px; }
  .card--back { top: 617px; }

  .gold-script {
    position: absolute;
    left: 0; right: 0;
    text-align: center;
    font-family: "Norican", cursive;
    font-weight: 400;
    white-space: nowrap;
    color: var(--gold);
    background: linear-gradient(180deg, var(--gold-light) 0%, var(--gold) 50%, var(--gold-deep) 100%);
    -webkit-background-clip: text;
    background-clip: text;
    -webkit-text-fill-color: transparent;
    filter: drop-shadow(-2px 2px 0 var(--shadow));
  }
  .website {
    position: absolute;
    left: 0; right: 0;
    text-align: center;
    font-family: "Dancing Script", cursive;
    font-weight: 500;
    color: var(--ink);
    white-space: nowrap;
  }

  .card--front .name { top: 150px; font-size: 38px; letter-spacing: -0.5px; }
  .card--front .title { top: 248px; font-size: 19px; }
  .card--front .website { top: 281px; font-size: 12px; }

  .card-back-frame { position: absolute; left: 0; top: 0; width: 342px; height: 444px; }
  .card--back .name { top: 196px; font-size: 23px; letter-spacing: -0.4px; }
  .card--back .title { top: 233px; font-size: 17px; }
  .card--back .website { top: 264px; font-size: 12px; }
</style>
</head>
<body>
<main class="canvas">
  <section class="card card--front" aria-label="Card front">
    <h1 class="gold-script name">Dorian Feldhaus</h1>
    <p class="gold-script title">Illusionist</p>
    <p class="website">www.FeldWonders.com</p>
  </section>

  <section class="card card--back" aria-label="Card back">
    <svg class="card-back-frame" viewBox="0 0 342 444" role="img" aria-label="Symmetrical playing-card back with scrollwork corners, star medallions and patterned border bands around an open centre">
      <defs>
        <radialGradient id="ornament-tone" cx="50%" cy="50%" r="65%">
          <stop offset="0%" stop-color="var(--ink-soft)"/>
          <stop offset="100%" stop-color="var(--ink)"/>
        </radialGradient>
      </defs>
      <!-- ornament field with open centre -->
      <path fill="url(#ornament-tone)" fill-opacity="0.72" fill-rule="evenodd"
        d="M30 20 H312 V424 H30 Z
           M150 62 Q171 56 192 62 Q240 110 250 180 Q256 222 250 264 Q240 334 192 382 Q171 388 150 382 Q102 334 92 264 Q86 222 92 180 Q102 110 150 62 Z"/>
      <!-- border bands -->
      <g fill="none" stroke="var(--card)">
        <rect x="36" y="26" width="270" height="392" stroke-width="1.5"/>
        <rect x="48" y="38" width="246" height="368" stroke-width="3"/>
        <rect x="62" y="52" width="218" height="340" stroke-width="1.2"/>
        <line x1="36" y1="222" x2="62" y2="222" stroke-width="2"/>
        <line x1="280" y1="222" x2="306" y2="222" stroke-width="2"/>
        <line x1="171" y1="26" x2="171" y2="52" stroke-width="2"/>
        <line x1="171" y1="392" x2="171" y2="418" stroke-width="2"/>
      </g>
      <!-- corner and medallion rings -->
      <g fill="none" stroke="var(--card)" stroke-width="1.5">
        <circle cx="62" cy="52" r="16"/>
        <circle cx="280" cy="52" r="16"/>
        <circle cx="62" cy="392" r="16"/>
        <circle cx="280" cy="392" r="16"/>
        <circle cx="104" cy="168" r="20"/>
        <circle cx="238" cy="168" r="20"/>
        <circle cx="104" cy="276" r="20"/>
        <circle cx="238" cy="276" r="20"/>
      </g>
      <!-- outline of open centre -->
      <path fill="none" stroke="var(--ink)" stroke-width="1.5"
        d="M150 62 Q171 56 192 62 Q240 110 250 180 Q256 222 250 264 Q240 334 192 382 Q171 388 150 382 Q102 334 92 264 Q86 222 92 180 Q102 110 150 62 Z"/>
    </svg>
    <h2 class="gold-script name">Dorian Feldhaus</h2>
    <p class="gold-script title">Illusionist</p>
    <p class="website">www.FeldWonders.com</p>
  </section>
</main>
</body>
</html>
```